Valbrook Data Works

Our company is about IT hardwares and IT solutions. IT hardware such as PC, RAMS, storage and servers. IT solutions such as project management, BA. We are also selling new technology too.

Target Market(s)

Consumer, Small to Medium Business, Corporate

Requirements
Must have
• The business card must have the following:
• Name:
• Title:
• Contact Number:
• Email address:
• Website:
• Color: Must match the logo color upgrade

```html
<!DOCTYPE html>
<html lang="en">
<head>
<meta charset="utf-8">
<title>Valbrook Data Works — Business Card</title>
<link rel="stylesheet" href="https://fonts.googleapis.com/css2?family=Work+Sans:wght@400;500;700&display=swap">
<style>
  :root {
    --stage: #2b2c2e;
    --card-white: #ffffff;
    --card-shade: #ececec;
    --ink: #3a3a3c;
    --ink-soft: #505052;
    --amber: #d8892f;
    --amber-light: #d2953c;
    --amber-deep: #b2571f;
    --silver: #d9d9db;
  }
  * { box-sizing: border-box; margin: 0; padding: 0; }
  html, body { width: 1200px; height: 900px; overflow: hidden; }
  body {
    background: var(--stage);
    font-family: "Work Sans", Arial, sans-serif;
    display: flex;
    flex-direction: column;
    align-items: center;
    justify-content: center;
    gap: 44px;
  }
  .card {
    width: 630px;
    height: 360px;
    border-radius: 22px;
    position: relative;
    overflow: hidden;
    box-shadow: 0 10px 24px rgba(0,0,0,.45);
  }
  .card--front {
    background: linear-gradient(135deg, var(--card-shade) 0%, var(--card-white) 45%, var(--card-white) 100%);
    display: flex;
    align-items: center;
  }
  .brand {
    width: 330px;
    display: flex;
    align-items: center;
    justify-content: center;
    gap: 14px;
  }
  .brand__dot {
    width: 26px; height: 26px;
    border-radius: 50%;
    background: var(--amber);
    flex: none;
  }
  .brand__name {
    font-weight: 700;
    font-size: 30px;
    line-height: 1.05;
    color: var(--ink);
    text-transform: uppercase;
    letter-spacing: .5px;
  }
  .divider {
    width: 2px;
    height: 170px;
    background: var(--amber);
    flex: none;
  }
  .contact {
    padding-left: 28px;
    color: var(--ink);
    font-size: 15px;
    line-height: 1.4;
  }
  .contact__name {
    font-size: 25px;
    font-weight: 500;
    color: var(--amber);
    text-transform: uppercase;
    line-height: 1.1;
  }
  .contact__title { font-size: 15px; color: var(--ink-soft); margin-bottom: 12px; }
  .contact__address { margin-bottom: 10px; }
  .contact__row { display: flex; align-items: center; gap: 8px; }
  .contact__row svg { width: 12px; height: 12px; flex: none; }
  .accent { color: var(--amber); }
  .card--back {
    background: linear-gradient(120deg, var(--amber-light) 0%, var(--amber-deep) 100%);
    display: flex;
    align-items: center;
    justify-content: center;
    gap: 18px;
  }
  .card--back .brand__dot { background: var(--silver); width: 34px; height: 34px; }
  .card--back .brand__name { color: var(--silver); font-size: 40px; }
</style>
</head>
<body>
  <section class="card card--front" aria-label="Business card front">
    <div class="brand">
      <span class="brand__dot"></span>
      <span class="brand__name">Valbrook<br>Data Works</span>
    </div>
    <span class="divider"></span>
    <div class="contact">
      <p class="contact__name">Daniel Hartley</p>
      <p class="contact__title">Director</p>
      <p class="contact__address">2280 Marlow Creek Rd<br>Alder, CA 95712-3048</p>
      <p class="contact__row">
        <svg viewBox="0 0 12 12" aria-hidden="true"><path d="M3 1 L5 3.5 L4 5 Q5 7 7 8 L8.5 7 L11 9 L9.5 11 Q5 11 1 5 Q1 2.5 3 1Z" fill="var(--amber)"/></svg>
        555-204-7731
      </p>
      <p class="contact__row">
        <svg viewBox="0 0 12 12" aria-hidden="true"><rect x="1" y="2.5" width="10" height="7" rx="1" fill="none" stroke="var(--amber)" stroke-width="1.2"/><path d="M1.5 3 L6 6.5 L10.5 3" fill="none" stroke="var(--amber)" stroke-width="1.2"/></svg>
        info@valbrookdata.com
      </p>
      <p class="contact__row">
        <svg viewBox="0 0 12 12" aria-hidden="true"><circle cx="6" cy="6" r="5" fill="none" stroke="var(--amber)" stroke-width="1.2"/><ellipse cx="6" cy="6" rx="2.2" ry="5" fill="none" stroke="var(--amber)" stroke-width="1"/><path d="M1 6 H11" stroke="var(--amber)" stroke-width="1"/></svg>
        www.<span class="accent">valbrookdata</span>.com
      </p>
    </div>
  </section>

  <section class="card card--back" aria-label="Business card back">
    <span class="brand__dot"></span>
    <span class="brand__name">Valbrook<br>Data Works</span>
  </section>
</body>
</html>
```